Robotic Physical Therapy office needs a Grand Opening Flyer

We need a Grand Opening flyer design for a robotic physical therapy office named Stellar Motion Therapy. We would like it to have a clean, classy, upscale feeling that gives potential clients a V.I.P. feeling. We would like to use the colors black, gray, and yellow (logo will be uploaded).

Event: Thursday, June 1st, 2023 from 12pm-6pm
location: 58274 Harlow Ave, Bloomfield Hills, MI 48319

Industry/Entity Type

Physical therapy

Font styles to use
Script

Colors

Designer to choose colors to be used in the design.

Requirements
Nice to have
• More of a vip feel for the invite

```html
<!DOCTYPE html>
<html lang="en">
<head>
<meta charset="UTF-8">
<title>Stellar Motion Therapy — Grand Opening</title>
<link href="https://fonts.googleapis.com/css2?family=Jost:wght@400;500;600;700&display=swap" rel="stylesheet">
<style>
  :root {
    --ink: #0b0b0b;
    --charcoal: #262626;
    --white: #ffffff;
    --yellow: #f8dd2e;
  }
  * { margin: 0; padding: 0; box-sizing: border-box; }
  html, body { width: 912px; height: 1200px; overflow: hidden; background: var(--ink); }
  .flyer {
    position: relative;
    width: 912px;
    height: 1200px;
    overflow: hidden;
    background: radial-gradient(ellipse at 50% 35%, var(--charcoal) 0%, #161616 55%, var(--ink) 100%);
    font-family: "Jost", "Futura", sans-serif;
    color: var(--white);
    text-align: center;
  }
  .frame-outer {
    position: absolute;
    inset: 8px;
    border: 4px solid var(--white);
  }
  .frame-inner {
    position: absolute;
    inset: 26px;
    border: 3px solid var(--white);
  }
  .backdrop-art {
    position: absolute;
    left: 90px; top: 300px;
    width: 732px; height: 760px;
    border-radius: 50%;
    background: radial-gradient(circle at 50% 50%, rgba(90,90,90,0.28) 0%, rgba(60,60,60,0.12) 45%, rgba(0,0,0,0) 70%);
  }
  .brand {
    position: absolute;
    top: 166px; left: 0; width: 100%;
    display: flex; justify-content: center; align-items: center; gap: 12px;
  }
  .brand-dot {
    width: 34px; height: 34px; border-radius: 50%;
    background: var(--yellow);
  }
  .brand-name {
    font-weight: 600;
    font-size: 34px;
    letter-spacing: 0.5px;
    color: var(--yellow);
    text-transform: uppercase;
    line-height: 1;
  }
  .headline { position: absolute; left: 0; width: 100%; line-height: 1; text-transform: uppercase; }
  .headline-grand {
    top: 372px;
    font-weight: 400;
    font-size: 150px;
    color: var(--white);
  }
  .headline-opening {
    top: 505px;
    font-weight: 700;
    font-size: 138px;
    color: var(--yellow);
  }
  .date-box {
    position: absolute;
    left: 139px; top: 683px;
    width: 634px; height: 99px;
    border: 1.5px solid var(--white);
    border-bottom: none;
  }
  .date-box::before, .date-box::after {
    content: ""; position: absolute; bottom: 0; height: 1.5px; background: var(--white);
    width: 152px;
  }
  .date-box::before { left: 0; }
  .date-box::after { right: 0; }
  .event-date {
    position: absolute; top: 14px; left: 0; width: 100%;
    font-weight: 500; font-size: 46px; line-height: 1;
    letter-spacing: 0.3px;
  }
  .event-time {
    position: absolute; bottom: -18px; left: 0; width: 100%;
    font-weight: 500; font-size: 35px; line-height: 1;
  }
  .address {
    position: absolute; top: 1014px; left: 0; width: 100%;
    font-style: normal;
    font-weight: 500; font-size: 31px; line-height: 1.15;
    text-transform: uppercase;
  }
</style>
</head>
<body>
<main class="flyer">
  <div class="backdrop-art" role="img" aria-label="Faint background artwork of a robotic hand surrounded by medical technology icons"></div>

  <div class="frame-outer" aria-hidden="true"></div>
  <div class="frame-inner" aria-hidden="true"></div>

  <header class="brand">
    <span class="brand-dot"></span>
    <span class="brand-name">Stellar Motion Therapy</span>
  </header>

  <h1 class="headline headline-grand">Grand</h1>
  <h2 class="headline headline-opening">Opening</h2>

  <section class="date-box">
    <p class="event-date">THURSDAY, JUNE 1ST, 2023</p>
    <p class="event-time">FROM 12PM-6PM</p>
  </section>

  <address class="address">58274 Harlow Ave, Bloomfield<br>Hills, MI 48319</address>
</main>
</body>
</html>
```